Webdesign für Maklerbüro
Zielgruppe
Wir sind ein Maklerbüro aus Nürnberg, das sich auf den Verkauf von Eigentumswohnungen und Häuser spezialisiert hat. Mit der neuen Seite möchten wir vor allem Eigentümer ansprechen und über unsere Arbeitsweise informieren. Der Hauptzweck ist damit die Akquise von neuen Objekten, für die Vermittlung. Die Zielgruppe sind vornehmlich Immobilienbesitzer im Alter 40+ und im gehobenen Preissegment.
Aufgabenstellung
Beim Design bitte an den Vorgaben des Logo (Datei beigefügt) orientieren. Bilder und Texte können durch 'Platzhalter' ersetzt werden.
Grundsätzlich stellt es für uns kein Problem dar, sich an Template-Vorlagen zu orientieren. Wir stellen uns eine Seite mit Pfiff und Ideenreichtum – einfach weg vom Standard – vor. Wir verkaufen Immobilien, aber vom verstaubten Krawattenträger sind wir weit entfernt. Wir sind ein junges Unternehmen, das neue Marketingwege beschreitet. Unsere Webseite muss das ausdrücken. Kein Standard, und damit auch keine Standard-Webseite. Designs, die uns gut gefallen (und in die Richtung es auch gehen kann) haben wir beigefügt.

```html
<!DOCTYPE html>
<html lang="de">
<head>
<meta charset="utf-8">
<title>Stadtwert Immo – Angebote</title>
<link href="https://fonts.googleapis.com/css2?family=Source+Sans+3:wght@400;600;700&display=swap" rel="stylesheet">
<style>
:root{
  --bg:#e0e0e0;
  --navy:#172039;
  --blue:#0a93d3;
  --white:#ffffff;
}
*{margin:0;padding:0;box-sizing:border-box}
html,body{width:1200px;height:2196px;overflow:hidden;background:var(--white)}
body{font-family:"Source Sans 3",sans-serif;color:var(--navy);position:relative}
.page{position:absolute;left:0;top:0;width:1200px;height:2043px;background:var(--bg)}
.abs{position:absolute}
.brand{left:118px;top:54px;font-size:31px;font-weight:700;letter-spacing:1px;display:flex;align-items:center;gap:10px}
.brand-mark{width:18px;height:18px;background:var(--blue)}
.nav{top:36px;left:437px;display:flex;gap:32px;font-size:20px}
.nav a{color:var(--navy);text-decoration:none;padding-bottom:2px}
.nav a.active{color:var(--blue);border-bottom:2px solid var(--blue)}
.hero{left:0;top:154px;width:1200px;height:285px;background:linear-gradient(90deg,#8c8f96 0%,#c7ccd3 25%,#9aa3ad 45%,#a07258 70%,#8c8c9b 100%)}
.hero-bar{left:0;top:439px;width:1200px;height:19px;background:var(--navy)}
.hero-bar span{position:absolute;left:0;top:0;width:137px;height:19px;background:var(--blue)}
.title{top:476px;left:0;width:1200px;text-align:center;font-size:30px}
.row{left:0;width:1200px;height:60px}
.row .label{position:absolute;width:220px;text-align:center;font-size:26px;line-height:26px}
.row .label small{display:block;font-size:19px;line-height:24px}
.row .icon{position:absolute;top:8px}
.row .val{position:absolute;top:14px;font-size:26px}
sup{font-size:14px}
.interest{left:283px;top:812px;font-size:25px}
.btn{left:697px;top:806px;width:216px;height:40px;background:var(--navy);border-bottom:5px solid var(--blue);color:var(--white);font-size:20px;text-align:center;line-height:36px}
.map{left:0;top:878px;width:1200px;height:220px;background:linear-gradient(120deg,#d9d6cc 0%,#9fc3ee 35%,#d7d3c8 55%,#a9c9ea 75%,#8ab8f0 100%)}
.about{left:0;top:1098px;width:1200px;height:402px;background:var(--navy);color:var(--white);padding:33px 99px 0}
.about p{font-size:19.4px;line-height:35.1px;text-align:justify}
.contact-title{top:1520px;left:0;width:1200px;text-align:center;font-size:31px}
.info{left:110px;font-size:16px;line-height:27px}
.info svg{position:absolute;left:0}
.info span{position:absolute;left:85px;white-space:nowrap}
.field{background:var(--navy);border-right:6px solid var(--blue);color:var(--white);font-size:15px;padding:0 16px;line-height:34px}
.footer{left:0;top:1996px;width:1200px;height:47px;background:var(--navy);color:var(--white);font-size:18px;display:flex;justify-content:center;gap:56px;line-height:47px}
</style>
</head>
<body>
<div class="page">
  <div class="abs brand"><span class="brand-mark"></span>STADTWERT IMMO</div>
  <nav class="abs nav">
    <a href="#">Home</a><a href="#">Eigentümer</a><a href="#">Bewertung</a><a href="#">Beratung</a><a href="#" class="active">Angebote</a><a href="#">Kontakt</a>
  </nav>

  <div class="abs hero" role="img" aria-label="Modernes Badezimmer mit zwei Waschbecken und Fensterblick auf Berge"></div>
  <div class="abs hero-bar"><span></span></div>

  <h1 class="abs title" style="font-weight:400">“Lindengarten”</h1>

  <svg width="0" height="0" style="position:absolute">
    <defs>
      <g id="plan" fill="none" stroke="#172039" stroke-width="1.5"><rect x="2" y="2" width="40" height="40"/><rect x="7" y="7" width="30" height="30"/><path d="M7 20h12v17M19 12v8M26 7v12h11M26 26h11"/></g>
      <g id="door" fill="none" stroke="#172039" stroke-width="1.5"><rect x="2" y="4" width="28" height="40"/><path d="M2 4l16-4v44"/><circle cx="14" cy="24" r="1.2" fill="#172039"/></g>
      <g id="house" fill="none" stroke="#172039" stroke-width="1.5"><path d="M2 20L22 4l20 16M7 16v24h22M12 40V28h8v12M28 8v4"/><circle cx="36" cy="36" r="9"/><text x="32" y="41" font-size="13" fill="#172039" stroke="none" font-family="sans-serif">$</text></g>
    </defs>
  </svg>

  <div class="abs row" style="top:536px">
    <div class="label" style="left:177px">Gartenwohnung<small>Neubau, EG</small></div>
    <svg class="icon" style="left:445px" width="46" height="46"><use href="#plan"/></svg>
    <div class="val" style="left:513px">78m<sup>2</sup></div>
    <svg class="icon" style="left:627px" width="32" height="46"><use href="#door"/></svg>
    <div class="val" style="left:681px">2 Zimmer</div>
    <svg class="icon" style="left:838px" width="46" height="46"><use href="#house"/></svg>
    <div class="val" style="left:906px">329.000€</div>
  </div>
  <div class="abs row" style="top:625px">
    <div class="label" style="left:177px">Maisonette<small>Neubau, 1. - 2. OG</small></div>
    <svg class="icon" style="left:445px" width="46" height="46"><use href="#plan"/></svg>
    <div class="val" style="left:513px">114m<sup>2</sup></div>
    <svg class="icon" style="left:627px" width="32" height="46"><use href="#door"/></svg>
    <div class="val" style="left:681px">3 Zimmer</div>
    <svg class="icon" style="left:838px" width="46" height="46"><use href="#house"/></svg>
    <div class="val" style="left:906px">469.000€</div>
  </div>
  <div class="abs row" style="top:714px">
    <div class="label" style="left:171px">Gartenwohnung<small>Neubau, EG</small></div>
    <svg class="icon" style="left:447px" width="46" height="46"><use href="#plan"/></svg>
    <div class="val" style="left:515px">140m<sup>2</sup></div>
    <svg class="icon" style="left:627px" width="32" height="46"><use href="#door"/></svg>
    <div class="val" style="left:681px">5 Zimmer</div>
    <svg class="icon" style="left:836px" width="46" height="46"><use href="#house"/></svg>
    <div class="val" style="left:904px">529.000€</div>
  </div>

  <div class="abs interest">Interesse an einem der Objekte?</div>
  <div class="abs btn">Exposé anfordern</div>

  <div class="abs map" role="img" aria-label="Stadtplan mit Lage des Objekts"></div>

  <section class="abs about">
    <p>Lorem ipsum dolor sit amet, consectetur adipiscing elit. Sed faucibus libero egestas lorem euismod gravida. Nullam et ultrices ipsum. Cras semper turpis ut pellentesque aliquet. Praesent at pulvinar justo. Duis ultrices pellentesque vestibulum. Integer nec enim ac ligula lobortis dictum. Vestibulum sit amet dolor et mauris fermentum commodo. Proin rhoncus sit amet diam tincidunt sagittis. Quisque fringilla, est a tincidunt mattis, turpis quam convallis sapien, quis pulvinar nulla lacus quis erat. Interdum et malesuada fames ac ante ipsum primis in faucibus. Etiam suscipit convallis cursus. Aliquam lacinia, eros a convallis porta, enim nisl aliquam dolor, sit amet egestas ante mauris et enim. Integer condimentum ligula in ullamcorper cursus. Curabitur mollis semper justo, ac dignissim odio euismod sed. Donec quis mauris at justo aliquam eleifend vel in neque. orem ipsum dolor sit amet, consectetur adipiscing elit. Sed faucibus libero egestas lorem euismod gravida. Nullam et ultrices ipsum. Cras semper turpis ut pellentesque aliquet. Praesent at pulvinar justo. Duis ultrices pellentesque vestibulum. Integer nec enim ac ligula lobortis dictum. Vestibu-</p>
  </section>

  <h2 class="abs contact-title" style="font-weight:400">Treten Sie mit Uns in Kontakt.</h2>

  <div class="abs info" style="top:1616px">
    <svg width="44" height="46" fill="none" stroke="#172039" stroke-width="1.5"><rect x="4" y="2" width="22" height="42"/><rect x="26" y="20" width="14" height="24"/><path d="M9 8h4M17 8h4M9 15h4M17 15h4M9 22h4M17 22h4M9 29h4M17 29h4M30 27h6M30 34h6M12 44v-7h6v7"/></svg>
    <span style="top:0">Lindenhofstraße 24<br>90482 Nürnberg</span>
  </div>
  <div class="abs info" style="top:1706px">
    <svg width="46" height="46" fill="none" stroke="#172039" stroke-width="1.6"><path d="M8 2l8 10-5 5c3 7 9 13 16 16l5-5 10 8-5 7C20 42 4 26 2 8z"/></svg>
    <span style="top:14px">+49 911 5550 27 14</span>
  </div>
  <div class="abs info" style="top:1794px">
    <svg width="46" height="46" fill="none" stroke="#172039" stroke-width="1.6"><rect x="9" y="1" width="28" height="44" rx="4"/><path d="M9 8h28M9 37h28"/><circle cx="23" cy="41" r="1" fill="#172039"/></svg>
    <span style="top:14px">+49 170 5552 83 09</span>
  </div>
  <div class="abs info" style="top:1884px">
    <svg width="46" height="32" fill="none" stroke="#172039" stroke-width="1.6"><rect x="1" y="1" width="44" height="30"/><path d="M1 1l22 18L45 1M1 31l16-16M45 31L29 15"/></svg>
    <span style="top:2px">kontakt@stadtwert-immo.de</span>
  </div>

  <div class="abs field" style="left:529px;top:1617px;width:268px">Ihr Name*</div>
  <div class="abs field" style="left:837px;top:1617px;width:268px">Straße, Hausnummer*</div>
  <div class="abs field" style="left:529px;top:1670px;width:268px">E-Mail*</div>
  <div class="abs field" style="left:837px;top:1670px;width:268px">Postleitzahl, Ort*</div>
  <div class="abs field" style="left:529px;top:1729px;width:576px;height:194px;padding-top:8px;line-height:20px">Ihre Nachricht an Uns.</div>

  <footer class="abs footer"><span>Impressum</span><span>Datenschutz</span></footer>
</div>
</body>
</html>
```